Business Cards & Stationery for a Gold Refiner
Brambleton Assets
Business Cards & Stationery for a Gold Refiner - Jewelry
Creative Brief
Professional
(MUST BE LEFT BLANK)
18 East 52nd Street, Lobby Rear, New York, NY 10022
(212)-584-MINT (6468)
info@brambletonassetsllc.example
Hey Designers, We would like for our telephone, fax, and email to be titled with symbols instead of words, e.g. a small telephone symbol next to the phone number and a fax machine next to the fax number. We require blank fields we can fill in, with no symbols, for: NAME, TITLE We require blank fields we can fill in, with symbols, for: CELL NUMBER, EMAIL, WEB ADDRESS Also, and this point is VERY IMPORTANT, we need the final deliverables to include an editable Adobe Illustrator and/or Photoshop file (preferably, Illustrator). We will include the names and titles of our individual employees ourselves, thus we need those sections to be left blank. All fields should be editable. We will not accept the design if it does not include a fully editable file. Our logo was recently completed and we require it to be included in the design. The file should be attached to the contest. We have additional versions of the logo we'd like to be able to swap out at will, however they are all in the same style as the logo provided, so the color scheme of the logo should be utilized throughout. The font should be traditional and corporate in style, and not too stylized or flashy. The logo should be included on the back as well. Thanks Everybody and Good Luck!

```html
<!DOCTYPE html>
<html lang="en">
<head>
<meta charset="utf-8">
<title>Brambleton Assets – Business Cards</title>
<link href="https://fonts.googleapis.com/css2?family=Roboto:wght@400;700;900&display=swap" rel="stylesheet">
<style>
  :root {
    --gold: #c99e0f;
    --white: #ffffff;
    --grey-light: #bdbdbd;
    --backdrop: #e9e6e0;
  }
  * { margin: 0; padding: 0; box-sizing: border-box; }
  html, body { width: 1200px; height: 799px; overflow: hidden; }
  body {
    background: var(--backdrop);
    font-family: "Roboto", Arial, sans-serif;
    position: relative;
  }
  .card {
    position: absolute;
    width: 520px;
    height: 300px;
    border-radius: 22px;
    overflow: hidden;
    box-shadow: 0 10px 28px rgba(0,0,0,0.18);
  }
  .brand { display: flex; align-items: center; gap: 12px; }
  .brand-mark { width: 44px; height: 44px; background: currentColor; flex: none; }
  .brand-name {
    font-weight: 900; line-height: 1; letter-spacing: 0.5px;
    text-transform: uppercase;
  }
  /* Front */
  .card-front {
    left: 50px; top: 250px;
    background: var(--gold);
    display: flex; flex-direction: column; justify-content: center; align-items: center;
    color: var(--white);
  }
  .card-front .brand-name { font-size: 30px; }
  .social-row { display: flex; gap: 7px; margin-top: 16px; }
  .social-row span { width: 15px; height: 15px; background: var(--white); border-radius: 3px; }
  .front-web { margin-top: 10px; font-size: 12px; font-weight: 400; }
  /* Back */
  .card-back { left: 630px; top: 250px; background: var(--white); }
  .card-back svg.wave { position: absolute; inset: 0; }
  .back-brand {
    position: absolute; left: 22px; top: 158px; color: var(--gold); gap: 10px;
  }
  .back-brand .brand-mark { width: 38px; height: 38px; }
  .back-brand .brand-name { font-size: 20px; line-height: 1.05; }
  .contact {
    position: absolute; right: 24px; top: 28px; text-align: right; color: var(--white);
  }
  .person-name { font-size: 17px; font-weight: 700; }
  .person-title { font-size: 11px; margin-top: 2px; }
  .contact-list { list-style: none; margin-top: 36px; font-size: 10.5px; line-height: 1.55; }
  .contact-list li { display: flex; justify-content: flex-end; align-items: center; gap: 8px; }
  .contact-list li::after {
    content: ""; width: 9px; height: 9px; border-radius: 50%; background: var(--white); flex: none;
  }
  .contact-list li.plain::after { background: transparent; }
</style>
</head>
<body>

<section class="card card-front" aria-label="Card front">
  <div class="brand">
    <span class="brand-mark"></span>
    <span class="brand-name">Brambleton Assets</span>
  </div>
  <div class="social-row" aria-label="Social links">
    <span></span><span></span><span></span><span></span>
  </div>
  <p class="front-web">www.brambletonassetsllc.example</p>
</section>

<section class="card card-back" aria-label="Card back">
  <svg class="wave" width="520" height="300" viewBox="0 0 520 300">
    <path d="M232 0 C 332 60, 182 200, 292 300 L520 300 L520 0 Z" fill="var(--gold)"/>
    <path d="M218 0 C 318 60, 168 200, 278 300" fill="none" stroke="var(--grey-light)" stroke-width="10"/>
  </svg>
  <div class="back-brand brand">
    <span class="brand-mark"></span>
    <span class="brand-name">Brambleton<br>Assets</span>
  </div>
  <div class="contact">
    <p class="person-name">Dana Whitlow</p>
    <p class="person-title">President</p>
    <ul class="contact-list">
      <li>18 East 52nd Street, Lobby Rear</li>
      <li class="plain">New York, NY 10022</li>
      <li>(212)-584-MINT (6468)</li>
      <li>(212) 584-2210</li>
      <li>(212) 584-2211</li>
      <li>info@brambletonassetsllc.example</li>
      <li>www.brambletonassetsllc.example</li>
    </ul>
  </div>
</section>

</body>
</html>
```